Pebblestone Promotions Flyer Design

I need to be able to have a flyer that shows what I do for businesses. Same logo that you designed.

Requirements
Must have
• I gave an example of what I need it to say in the attachment. Must have logo and resemble business card style.
Nice to have
• It could include pictures of what a digital sign is. We offer an KVRT, weather, and news slide on our advertising. I included sample pictures of those.

```html
<!DOCTYPE html>
<html lang="en">
<head>
<meta charset="utf-8">
<title>Pebblestone Promotions Flyer</title>
<link rel="stylesheet" href="https://fonts.googleapis.com/css2?family=Dosis:wght@300;400;500;600&display=swap">
<style>
  :root {
    --ink: #2a2a2a;
    --charcoal: #353535;
    --paper: #f7f7f7;
    --green: #7dc242;
    --white: #ffffff;
    --logo-grey: #5b5b5b;
    --screen-frame: #111111;
  }
  * { margin: 0; padding: 0; box-sizing: border-box; }
  html, body { width: 848px; height: 1200px; overflow: hidden; }
  body { background: var(--paper); font-family: "Dosis", sans-serif; color: var(--ink); }
  .flyer { position: relative; width: 848px; height: 1200px; overflow: hidden; background: var(--paper); }
  .shape { position: absolute; left: 0; top: 0; }
  .abs { position: absolute; }

  .brand { position: absolute; color: var(--logo-grey); font-weight: 600; line-height: 1; }
  .brand__name { display: block; }
  .brand__tag { display: block; text-transform: uppercase; }
  .brand--header { left: 26px; top: 20px; }
  .brand--header .brand__name { font-size: 58px; letter-spacing: -1px; }
  .brand--header .brand__tag { font-size: 17px; letter-spacing: 10px; margin-top: 2px; margin-left: 4px; }
  .brand--footer { left: 24px; top: 1161px; }
  .brand--footer .brand__name { font-size: 26px; letter-spacing: -0.5px; }
  .brand--footer .brand__tag { font-size: 8px; letter-spacing: 4.5px; margin-left: 2px; }

  .heading { position: absolute; color: var(--green); font-weight: 400; text-align: right; line-height: 1; }
  .heading--what { right: 26px; top: 142px; font-size: 26px; }
  .heading--benefits { right: 20px; top: 432px; font-size: 24px; color: var(--white); line-height: 0.82; }
  .heading--process { right: 14px; top: 808px; font-size: 25px; }

  .list { position: absolute; list-style: none; }
  .list li { position: relative; font-size: 14.5px; line-height: 14.2px; font-weight: 400; }
  .list li::before { content: ""; position: absolute; width: 17px; height: 17px; border-radius: 50%; background: var(--green); left: -27px; top: 50%; transform: translateY(-50%); }
  .list p { text-align: justify; text-align-last: left; }

  .list--what { left: 461px; top: 196px; width: 312px; color: var(--white); }
  .list--what li { margin-bottom: 14px; }

  .list--benefits { left: 110px; top: 478px; width: 311px; }
  .list--benefits li { margin-bottom: 15px; }
  .list--benefits li.big { font-size: 23px; line-height: 1; margin-top: 8px; }
  .you { position: absolute; left: 304px; top: 744px; font-size: 40px; line-height: 1; font-weight: 400; }

  .screen { position: absolute; background: var(--screen-frame); padding: 4px 4px 7px; }
  .screen__view { width: 100%; height: 100%; }
  .screen--news { left: 68px; top: 188px; width: 346px; height: 202px; }
  .screen--news .screen__view { background: linear-gradient(90deg, #3e4556 0%, #6b7483 42%, #f4f4f4 56%, #ffffff 100%); }
  .screen--weather { left: 451px; top: 503px; width: 331px; height: 184px; }
  .screen--weather .screen__view { background: linear-gradient(180deg, #3150cf 0%, #3a55d6 100%); }
  .reflection { position: absolute; left: 451px; top: 690px; width: 331px; height: 90px; background: linear-gradient(180deg, rgba(205,210,235,0.55), rgba(247,247,247,0)); }
  .reflection--news { left: 68px; top: 392px; width: 346px; height: 30px; background: linear-gradient(180deg, rgba(190,190,190,0.5), rgba(247,247,247,0)); }

  .strip { position: absolute; left: 509px; top: 898px; width: 339px; height: 112px; background: linear-gradient(90deg, #5a3a32 0%, #6f5a55 30%, #e8e8e8 38%, #f2f2f2 63%, #2d3a7a 68%, #3b4a8e 100%); }
  .strip-glow { position: absolute; left: 480px; top: 1010px; width: 368px; height: 143px; background: linear-gradient(180deg, rgba(120,120,120,0.55), rgba(53,53,53,0)); }

  .steps { position: absolute; left: 0; top: 0; }
  .step-num { position: absolute; width: 34px; height: 34px; border-radius: 50%; background: var(--green); color: var(--white); font-size: 26px; line-height: 34px; text-align: center; font-weight: 300; left: 66px; }
  .rail { position: absolute; left: 81px; top: 823px; width: 3px; height: 258px; background: var(--green); }
  .step-text { position: absolute; left: 106px; width: 335px; color: var(--white); font-size: 14.5px; line-height: 14.2px; text-align: justify; text-align-last: left; }

  .footer-line { position: absolute; left: 238px; top: 1163px; font-size: 19px; line-height: 1; white-space: nowrap; }
  .footer-line .accent { color: var(--green); }
  .dots { display: inline-block; border-bottom: 1px dotted var(--ink); height: 1px; vertical-align: 2px; }
</style>
</head>
<body>
<div class="flyer">

  <svg class="shape" width="848" height="1200" viewBox="0 0 848 1200" aria-hidden="true">
    <path d="M0,173 L420,173 C490,173 505,103 590,101 L790,101 L790,364 L0,364 Z" fill="var(--charcoal)" transform="translate(0,0)"/>
    <path d="M0,173 L410,173 C490,173 510,102 600,102 L848,102 L848,364 L0,364 Z" fill="#353535"/>
    <path d="M296,421 L848,421 L848,486 L560,486 C460,486 400,428 296,421 Z" fill="#7dc242"/>
    <path d="M0,785 L520,785 C585,785 590,846 660,846 L848,846 L848,1153 L0,1153 Z" fill="#353535"/>
  </svg>

  <div class="brand brand--header">
    <span class="brand__name">Pebblestone</span>
    <span class="brand__tag">Promotions</span>
  </div>

  <div class="heading heading--what">What We Do</div>

  <div class="screen screen--news">
    <div class="screen__view" role="img" aria-label="Digital sign showing a news slide with a winter storm photo and headline"></div>
  </div>
  <div class="reflection reflection--news"></div>

  <ul class="list list--what">
    <li><p>We provide monthly payments to businesses for allowing us to advertise local businesses on a TV screen in your place of business.</p></li>
    <li><p>We provide the TV screen if you prefer (professional installation on our dime)</p></li>
    <li><p>We provide a win/win for the businesses that partner with us. Our business partners get paid to support local businesses.</p></li>
  </ul>

  <div class="heading heading--benefits">Benefits of Partnering with<br>Pebblestone Promotions</div>

  <ul class="list list--benefits">
    <li><p>WE PAY YOU!</p></li>
    <li><p>We advertise local businesses and business owners. We encourage them to stop by your establishment to check out their ad. This will create more foot traffic to your business.</p></li>
    <li><p>Waiting Rooms: Studies show perceived wait time can be decreased by up to 33% when there is digital signage present. This can make your clients’ 60 min wait feel like a 40 min wait.</p></li>
    <li><p>Professional ticker at the bottom of the digital design can display sports updates, breaking news, and weather. Our design approach makes your business look more professional.</p></li>
    <li class="big"><p>Did we mention that we pay</p></li>
  </ul>
  <div class="you">You?!!!</div>

  <div class="screen screen--weather">
    <div class="screen__view" role="img" aria-label="Digital sign showing a weather slide with current temperature and forecast"></div>
  </div>
  <div class="reflection"></div>

  <div class="heading heading--process">Effortless Process</div>

  <div class="strip" role="img" aria-label="Digital sign showing a KVRT sports slide with player photos"></div>
  <div class="strip-glow"></div>

  <div class="rail"></div>
  <div class="step-num" style="top:823px">1</div>
  <div class="step-num" style="top:900px">2</div>
  <div class="step-num" style="top:983px">3</div>
  <div class="step-num" style="top:1065px">4</div>

  <div class="step-text" style="top:834px">Day 1: Sign on to partner with Pebblestone Promotions.</div>
  <div class="step-text" style="top:865px">Week 1: We install a HDMI/USB drive to the screen. Our onsite time for this is less than 10 minutes and this WILL NOT disrupt your business operations. In fact, you may not even notice we came and went. (We can use an existing screen or install a new screen at no cost to you if space permits)</div>
  <div class="step-text" style="top:976px">Week 1-8: We will be loading our local advertisers’ professional designs to the screen. (This is done remotely and does not require us to come in)</div>
  <div class="step-text" style="top:1071px">End of 2nd Full Month: Process is complete, and you will be receiving monthly checks!</div>
  <div class="step-text" style="top:1117px">Notice your involvement is only in the first and last step. Sign-up. Get Paid.</div>

  <div class="brand brand--footer">
    <span class="brand__name">Pebblestone</span>
    <span class="brand__tag">Promotions</span>
  </div>

  <div class="footer-line">We will <span class="accent">pay</span> you <span class="dots" style="width:118px"></span>each month. <span class="accent">Call</span> for details<span class="dots" style="width:110px"></span></div>

</div>
</body>
</html>
```